Global Weight loss program

we need a business card based in Brooklyn , NY called PeppertonRUN . Mara Dulvik Tenbrook the founder and creator of PeppertonRUN Movement. A business based around nutrition, health, Whole Foods and fitness.

Industry/Entity Type

Food Service

Contact Information for Business Card

Phone number : 718-555-0143
website www.peppertonrun.com
email : mara@peppertonrun.com

Font styles to use
Sans Serif

Requirements
Must have
• logo colors
• green black and gold
Nice to have
• must be simple and sharp.
Should not have
• pictures of items

```html
<!DOCTYPE html>
<html lang="en">
<head>
<meta charset="utf-8">
<title>PeppertonRUN – Business Card</title>
<link rel="stylesheet" href="https://fonts.googleapis.com/css2?family=Montserrat:wght@600;700&family=Questrial&display=swap">
<style>
  :root {
    --green: #8cb33e;
    --green-dark: #6c9130;
    --gold: #f5c000;
    --slate: #4f5058;
    --ink: #3b3e42;
    --white: #ffffff;
    --edge: #a3a3a3;
    --page: #ffffff;
  }
  * { margin: 0; padding: 0; box-sizing: border-box; }
  html, body {
    width: 1043px;
    height: 1200px;
    overflow: hidden;
    background: var(--page);
  }
  .card {
    position: absolute;
    left: 0;
    width: 1043px;
    height: 578px;
    border: 2px solid var(--edge);
    overflow: hidden;
    background: var(--white);
  }
  .card--front { top: 0; }
  .card--back { top: 622px; }
  .card__art {
    position: absolute;
    inset: 0;
    width: 100%;
    height: 100%;
  }
  .brand {
    position: absolute;
    text-align: center;
    font-family: "Montserrat", sans-serif;
    font-weight: 600;
    color: var(--ink);
    line-height: 1;
    white-space: nowrap;
  }
  .card--front .brand {
    left: 0;
    right: 0;
    top: 230px;
    font-size: 58px;
  }
  .card--back .brand {
    left: 30px;
    width: 320px;
    top: 322px;
    font-size: 36px;
  }
  .holder {
    position: absolute;
    right: 78px;
    top: 88px;
    font-family: "Montserrat", sans-serif;
    font-weight: 700;
    font-size: 41px;
    color: var(--gold);
    white-space: nowrap;
  }
  .contact {
    position: absolute;
    right: 73px;
    top: 370px;
    list-style: none;
    text-align: right;
    font-family: "Questrial", sans-serif;
    font-size: 36px;
    line-height: 49px;
    color: var(--gold);
    white-space: nowrap;
  }
</style>
</head>
<body>

<section class="card card--front">
  <svg class="card__art" viewBox="0 0 1043 578" aria-hidden="true">
    <rect x="0" y="0" width="1043" height="22" fill="var(--green)"/>
    <polygon points="145,578 532,374 902,578" fill="var(--gold)"/>
    <polygon points="0,433 180,460 213,512 145,578 0,578" fill="var(--green)"/>
    <polygon points="165,458 213,512 182,466" fill="var(--green-dark)"/>
    <polygon points="1043,433 863,460 830,512 902,578 1043,578" fill="var(--green)"/>
    <polygon points="878,458 830,512 861,466" fill="var(--green-dark)"/>
  </svg>
  <p class="brand">PeppertonRUN</p>
</section>

<section class="card card--back">
  <svg class="card__art" viewBox="0 0 1043 578" aria-hidden="true">
    <rect x="0" y="0" width="1043" height="578" fill="var(--slate)"/>
    <polygon points="0,0 120,0 478,287 120,578 0,578" fill="var(--white)"/>
    <rect x="1011" y="0" width="32" height="578" fill="var(--green)"/>
  </svg>
  <p class="brand">PeppertonRUN</p>
  <h1 class="holder">Mara Dulvik Tenbrook</h1>
  <ul class="contact">
    <li>Phone number : 718-555-0143</li>
    <li>website www.peppertonrun.com</li>
    <li>email : mara@peppertonrun.com</li>
  </ul>
</section>

</body>
</html>
```